"Oral Surgery Office needs a Business Card Design with Logo"

We need a logo design and business card. The name of the office is Tassingford Oral Surgery & Implant Center. The final design should communicate uniqueness as well as highly class office. The business card should emphasize power. I included the current business card below. Please design something unique

Target Market(s)

Dentists & Patients

Industry/Entity Type

Dental

Contact Information for Business Card

Unique Design to show success, prestige, Style, unmatched performance

Font styles to use
Serif

Colors
1b1b1b
ffffff
0556a4

Requirements
Must have
• Bussiness Name, Doctor's Name, Website, phone and Fax, email, office address
• Color should be either Black and White or Blue and White
Nice to have
• Clean look
Should not have
• the business card shouldn't be too busy. I feel like the old business card was too busy

```html
<!DOCTYPE html>
<html lang="en">
<head>
<meta charset="utf-8">
<title>Tassingford Oral Surgery &amp; Implant Center – Business Card</title>
<link href="https://fonts.googleapis.com/css2?family=Open+Sans:wght@400;600;700&display=swap" rel="stylesheet">
<style>
  :root {
    --ink: #1b1b1b;
    --black: #000000;
    --blue: #29a3dd;
    --paper: #ffffff;
    --backdrop: #e8e6e3;
  }
  * { margin: 0; padding: 0; box-sizing: border-box; }
  html, body { width: 1200px; height: 1000px; overflow: hidden; }
  body {
    position: relative;
    background: var(--backdrop);
    font-family: "Open Sans", Arial, sans-serif;
    color: var(--ink);
  }
  .card {
    position: absolute;
    left: 266px;
    width: 666px;
    height: 397px;
    background: var(--paper);
    overflow: hidden;
  }
  .card--front { top: 74px; }
  .card--back  { top: 534px; }

  .brand { position: absolute; display: flex; align-items: center; }
  .brand__mark { background: var(--ink); flex: none; }
  .brand__name {
    font-weight: 600;
    color: var(--ink);
    text-transform: uppercase;
    line-height: 1;
  }
  .brand__line { display: block; white-space: nowrap; }

  .card--front .brand { left: 32px; top: 31px; }
  .card--front .brand__mark { width: 104px; height: 106px; margin-right: 16px; }
  .card--front .brand__line--main { font-size: 17px; letter-spacing: 0.2px; }
  .card--front .brand__line--sub { font-size: 15px; letter-spacing: 6.3px; margin-top: 12px; }

  .card--back .brand { left: 107px; top: 137px; }
  .card--back .brand__mark { width: 120px; height: 122px; margin-right: 18px; }
  .card--back .brand__line--main { font-size: 19.5px; letter-spacing: 0.2px; }
  .card--back .brand__line--sub { font-size: 17px; letter-spacing: 7.4px; margin-top: 14px; }

  .doctor {
    position: absolute;
    right: 32px;
    top: 195px;
    text-align: right;
  }
  .doctor__name { font-size: 20px; font-weight: 600; color: var(--ink); }
  .doctor__name span { font-weight: 400; }
  .doctor__title { font-size: 15.5px; color: var(--blue); margin-top: 2px; }

  .contact {
    position: absolute;
    left: 33px;
    top: 221px;
    list-style: none;
    font-size: 16px;
  }
  .contact__item { display: flex; align-items: center; height: 23.3px; }
  .contact__item svg { width: 15px; height: 13px; margin-right: 8px; fill: var(--ink); }
  .contact__address { margin-top: 6px; font-size: 16px; }

  .band { position: absolute; left: 0; bottom: 0; }
</style>
</head>
<body>

<section class="card card--front">
  <div class="brand">
    <div class="brand__mark"></div>
    <div class="brand__name">
      <span class="brand__line brand__line--main">Tassingford Oral Surgery</span>
      <span class="brand__line brand__line--sub">&amp; Implant Center</span>
    </div>
  </div>

  <div class="doctor">
    <p class="doctor__name">Dr. Morris Elkavy<span>, D.D.S</span></p>
    <p class="doctor__title">Oral &amp; Maxillofacial Surgery</p>
  </div>

  <ul class="contact">
    <li class="contact__item">
      <svg viewBox="0 0 16 14" aria-hidden="true"><path d="M1 4c0-2 3-3 7-3s7 1 7 3v1h-3V4H4v1H1zM3 6h10l2 7H1zm5 1.5a2.3 2.3 0 1 0 0 4.6 2.3 2.3 0 0 0 0-4.6z"/></svg>
      555 - 014 - 2200
    </li>
    <li class="contact__item">
      <svg viewBox="0 0 16 14" aria-hidden="true"><path d="M4 0h8v4H4zM1 5h14v6h-2V9H3v2H1zM4 10h8v4H4z"/></svg>
      555 - 014 - 2290
    </li>
    <li class="contact__item">
      <svg viewBox="0 0 16 14" aria-hidden="true"><path d="M1 2h14v1L8 8 1 3zM1 5l7 5 7-5v7H1z"/></svg>
      tassingfordoralsurgery@mailbox.com
    </li>
    <li class="contact__item">
      <svg viewBox="0 0 16 14" aria-hidden="true"><path d="M1 1h14v9H1zm1.5 1.5v6h11v-6zM5 12h6v1.5H5z"/></svg>
      www.tassingfordoralsurgery.com
    </li>
    <li class="contact__address">2840 Harlow Street, Tassingford, NY 11290</li>
  </ul>

  <svg class="band" width="666" height="34" viewBox="0 0 666 34" aria-hidden="true">
    <polygon points="0,2 394,2 439,34 0,34" fill="var(--black)"/>
    <polygon points="420,12 666,12 666,34 448,34" fill="var(--blue)"/>
  </svg>
</section>

<section class="card card--back">
  <div class="brand">
    <div class="brand__mark"></div>
    <div class="brand__name">
      <span class="brand__line brand__line--main">Tassingford Oral Surgery</span>
      <span class="brand__line brand__line--sub">&amp; Implant Center</span>
    </div>
  </div>
</section>

</body>
</html>
```